Queldrin Engineering Brochure design

Need a brochure to promote our new industrial automation engineering firm. We would like a tech based robotics/mechanical design/electrical theme. Would like the general theme to match the company logo...sharp lines, colors, etc. Like the look of opaque content blocks with images in the background (see attached Plenforge design). The content needs to include everything on this attached design as a reference...these showcase our capabilities.
Updates

Project Deadline Extended
Reason: We have been busy and need more time to review...all good submissions!

Target Market(s)

Manufacturing plants, engineering departments

Industry/Entity Type

Manufacture

Font styles to use
Other font styles liked:
• really like "refrigerator deluxe" using all caps as much as possible. if not, like the aspect of all caps

Requirements
Must have
• company logo
• robotics references
• mechanical design references

```html
<!DOCTYPE html>
<html lang="en">
<head>
<meta charset="utf-8">
<title>Queldrin Engineering – Industrial Automation Brochure</title>
<link href="https://fonts.googleapis.com/css2?family=Oswald:wght@300;600&family=Lato:wght@400;700&display=swap" rel="stylesheet">
<style>
  :root {
    --navy: #1d3563;
    --ink: #2e2e2e;
    --slate: #4a4a4a;
    --panel-gray: #8c8c8c;
    --band-gray: #a9a9a9;
    --paper: #ffffff;
    --stage: #e6e6e6;
  }
  html, body {
    margin: 0;
    width: 1200px;
    height: 1200px;
    overflow: hidden;
    background: var(--stage);
  }
  .canvas {
    position: relative;
    width: 1200px;
    height: 1200px;
  }
  .cover {
    position: absolute;
    left: 170px;
    top: 47px;
    width: 801px;
    height: 1030px;
    background: var(--paper);
    transform: scale(1.074);
    transform-origin: 0 0;
    overflow: hidden;
    box-shadow: 0 4px 18px rgba(0,0,0,0.18);
  }
  .layer {
    position: absolute;
    left: 0;
    top: 0;
  }
  .brand {
    position: absolute;
    left: 36px;
    top: 54px;
    display: flex;
    align-items: center;
    gap: 12px;
    font-family: "Lato", sans-serif;
    font-weight: 700;
    color: var(--navy);
  }
  .brand-mark {
    width: 22px;
    height: 22px;
    background: var(--navy);
  }
  .brand-name {
    line-height: 1.05;
  }
  .brand-name .line-1 {
    display: block;
    font-size: 27px;
    letter-spacing: 0.5px;
  }
  .brand-name .line-2 {
    display: block;
    font-size: 15px;
    letter-spacing: 0.6px;
  }
  .headline {
    position: absolute;
    right: 34px;
    top: 46px;
    text-align: right;
    font-family: "Oswald", sans-serif;
    text-transform: uppercase;
    margin: 0;
  }
  .headline .main {
    display: block;
    font-weight: 600;
    font-size: 52px;
    line-height: 1.08;
    color: var(--navy);
    letter-spacing: -0.5px;
  }
  .headline .sub {
    display: block;
    font-weight: 300;
    font-size: 41px;
    line-height: 1.05;
    color: var(--ink);
    letter-spacing: -0.3px;
  }
  .contact {
    position: absolute;
    left: 77px;
    top: 694px;
    font-family: "Lato", sans-serif;
  }
  .contact-title {
    margin: 0 0 18px;
    font-size: 25px;
    font-weight: 400;
    line-height: 1.2;
    letter-spacing: 0.8px;
    text-transform: uppercase;
    color: var(--navy);
  }
  .contact-title .muted {
    display: block;
    color: var(--slate);
  }
  .contact-list {
    list-style: none;
    margin: 0;
    padding: 0;
  }
  .contact-list li {
    display: flex;
    align-items: flex-start;
    gap: 14px;
    color: var(--ink);
    font-size: 17px;
    line-height: 1.08;
    margin-bottom: 8px;
  }
  .contact-list .icon {
    width: 16px;
    height: 16px;
    flex: none;
    margin-top: 2px;
  }
  .contact-list .phone {
    font-size: 25px;
    color: var(--navy);
    line-height: 1;
  }
  .contact-list .phone .icon {
    margin-top: 4px;
  }
  .web-link {
    position: absolute;
    left: 40px;
    top: 932px;
    width: 340px;
    height: 45px;
    line-height: 45px;
    text-align: center;
    font-family: "Lato", sans-serif;
    font-size: 17px;
    color: var(--paper);
  }
</style>
</head>
<body>
<main class="canvas">
  <article class="cover">

    <!-- structural shapes -->
    <svg class="layer" width="801" height="1030" viewBox="0 0 801 1030" aria-hidden="true">
      <polygon points="0,196 347,196 322,232 0,232" fill="var(--navy)"/>
      <polygon points="580,628 801,628 801,985 390,985" fill="var(--panel-gray)"/>
      <rect x="0" y="985" width="801" height="5" fill="var(--paper)"/>
      <rect x="0" y="990" width="801" height="40" fill="var(--band-gray)"/>
      <polygon points="52,932 386,932 366,977 32,977" fill="var(--navy)"/>
    </svg>

    <!-- hero image area -->
    <svg class="layer" style="top:232px" width="801" height="413" viewBox="0 0 801 413" role="img" aria-label="Photo of yellow industrial robot arms assembling engine blocks on orange fixtures inside a fenced automation cell">
      <defs>
        <linearGradient id="hero-tone" x1="0" y1="0" x2="1" y2="1">
          <stop offset="0" stop-color="#9aa0a6"/>
          <stop offset="0.35" stop-color="#c9a93a"/>
          <stop offset="0.65" stop-color="#c7642a"/>
          <stop offset="1" stop-color="#6f7c8c"/>
        </linearGradient>
      </defs>
      <rect width="801" height="413" fill="url(#hero-tone)"/>
    </svg>
    <svg class="layer" style="top:628px;left:580px" width="221" height="17" viewBox="0 0 221 17" aria-hidden="true">
      <polygon points="0,0 221,0 221,17 -9,17" fill="var(--panel-gray)"/>
    </svg>

    <!-- inset image -->
    <svg class="layer" style="left:310px;top:670px" width="474" height="228" viewBox="0 0 474 228" role="img" aria-label="Photo of yellow welding robots working on a production line">
      <defs>
        <linearGradient id="inset-tone" x1="0" y1="0" x2="1" y2="1">
          <stop offset="0" stop-color="#5d6a55"/>
          <stop offset="0.45" stop-color="#d8b32a"/>
          <stop offset="1" stop-color="#4b5a6a"/>
        </linearGradient>
      </defs>
      <polygon points="84,4 470,4 392,224 4,224" fill="var(--paper)"/>
      <polygon points="90,10 461,10 387,218 13,218" fill="url(#inset-tone)"/>
    </svg>

    <!-- brand name -->
    <div class="brand">
      <span class="brand-mark"></span>
      <span class="brand-name">
        <span class="line-1">QUELDRIN</span>
        <span class="line-2">ENGINEERING INC.</span>
      </span>
    </div>

    <h1 class="headline">
      <span class="main">Industrial Automation</span>
      <span class="sub">Engineering Solutions</span>
    </h1>

    <section class="contact">
      <h2 class="contact-title">Contact<span class="muted">Information</span></h2>
      <ul class="contact-list">
        <li class="phone">
          <svg class="icon" viewBox="0 0 16 16" aria-hidden="true"><path d="M3.2 1.2l2.4 2.6-1.3 1.9c.9 2 2.4 3.5 4.4 4.4l1.9-1.3 2.6 2.4-1.4 2.4C6.5 13.4 2.6 9.5 1 3.2z" fill="var(--navy)"/></svg>
          <span>555-014-2276</span>
        </li>
        <li>
          <svg class="icon" viewBox="0 0 16 16" aria-hidden="true"><rect x="1.5" y="3.5" width="13" height="9" fill="none" stroke="var(--navy)" stroke-width="1.6"/><path d="M1.8 4l6.2 5 6.2-5" fill="none" stroke="var(--navy)" stroke-width="1.6"/></svg>
          <span>sales@queldrin.com</span>
        </li>
        <li>
          <svg class="icon" viewBox="0 0 16 16" aria-hidden="true"><path d="M8 1a5 5 0 0 1 5 5c0 3.6-5 9-5 9S3 9.6 3 6a5 5 0 0 1 5-5z" fill="var(--navy)"/><circle cx="8" cy="6" r="2" fill="var(--paper)"/></svg>
          <span>4820 Maplecrest Lane<br>Avondel, IN 46099</span>
        </li>
      </ul>
    </section>

    <div class="web-link">www.queldrinengineering.com</div>

  </article>
</main>
</body>
</html>
```